Poster Design for Photography Exhibit

We are looking for a poster design for a photography exhibit featuring high-end fashion and celebrity photography.

Name of the exhibit is "MILES DORVAN: UNTITLED" (please use Helvetica Black all cap for show name.

Poster is LANDSCAPE format (2 units wide by 1 unit high).

Unfortunately due to legal reasons, we cannot use any actual Miles Dorvan photos. No can we use fashions or people on the poster!

We are looking for a high-end, sexy, bold provocative design that captures the excitement and glamour of a fashion photo shoot.

Target Market(s)

Men and Women interested in Fashion Photography and art photography in general

Industry/Entity Type

Fashion

Requirements
Must have
• landscape format, name of exhibit in Helvetica Black all caps
Nice to have
• Can be grayscale or color.
Should not have
• Logos or brand names

```html
<!DOCTYPE html>
<html lang="en">
<head>
<meta charset="utf-8">
<title>Miles Dorvan : Untitled — Exhibition Poster</title>
<link rel="stylesheet" href="https://fonts.googleapis.com/css2?family=Archivo+Black&family=Arimo:wght@400&family=Parisienne&display=swap">
<style>
  :root {
    --bg: #000000;
    --ink: #ffffff;
    --cream: #efe4d8;
    --title: #f4f1ec;
    --bar: #4a3f9c;
  }
  * { margin: 0; padding: 0; box-sizing: border-box; }
  html, body {
    width: 1200px;
    height: 600px;
    overflow: hidden;
    background: var(--bg);
  }
  .poster {
    position: relative;
    width: 1200px;
    height: 600px;
    background: var(--bg);
    overflow: hidden;
    font-family: "Arimo", Helvetica, Arial, sans-serif;
    color: var(--ink);
  }
  .portrait {
    position: absolute;
    left: 0;
    top: 0;
    width: 470px;
    height: 600px;
    background:
      radial-gradient(ellipse 120px 180px at 80px 330px, rgba(98, 70, 190, 0.95), rgba(98, 70, 190, 0) 100%),
      radial-gradient(ellipse 230px 330px at 210px 330px, #e9d6c8 0%, #d9bca8 45%, rgba(120, 90, 75, 0.4) 80%, rgba(0,0,0,0) 100%),
      linear-gradient(180deg, #c9a888 0%, #8d6e58 20%, #1a1410 55%, #000 100%);
    -webkit-mask-image: linear-gradient(90deg, #000 70%, transparent 100%);
            mask-image: linear-gradient(90deg, #000 70%, transparent 100%);
  }
  .title-block {
    position: absolute;
    left: 446px;
    top: 143px;
  }
  .artist-name {
    font-family: "Archivo Black", "Helvetica Neue", Arial, sans-serif;
    font-size: 37px;
    line-height: 1;
    color: var(--cream);
    letter-spacing: -1.5px;
  }
  .show-name {
    display: block;
  }
  .show-name text {
    font-family: "Archivo Black", "Helvetica Neue", Arial, sans-serif;
    font-size: 142px;
    fill: var(--title);
  }
  .intro {
    position: absolute;
    right: 80px;
    top: 320px;
    width: 620px;
    text-align: right;
    font-size: 14.5px;
    line-height: 24px;
  }
  .dates {
    position: absolute;
    right: 80px;
    top: 412px;
    font-family: "Parisienne", cursive;
    font-size: 36px;
    line-height: 1;
    letter-spacing: 0.5px;
  }
  .dates-note {
    position: absolute;
    right: 80px;
    top: 459px;
    font-size: 14.5px;
    line-height: 1;
  }
  .web-bar {
    position: absolute;
    left: 720px;
    top: 522px;
    width: 480px;
    height: 21px;
    background: linear-gradient(90deg, rgba(74,63,156,0) 0%, var(--bar) 45%, var(--bar) 100%);
  }
  .web-address {
    position: absolute;
    right: 80px;
    top: 522px;
    height: 21px;
    line-height: 21px;
    font-size: 16px;
    letter-spacing: 1.2px;
  }
</style>
</head>
<body>
  <main class="poster">
    <div class="portrait" role="img" aria-label="Close-up fashion portrait in profile with violet eye make-up, fading into black"></div>

    <header class="title-block">
      <h2 class="artist-name">MILES DORVAN :</h2>
      <svg class="show-name" width="594" height="112" viewBox="0 0 594 112" aria-label="UNTITLED" role="img">
        <text x="0" y="105" textLength="590" lengthAdjust="spacingAndGlyphs">UNTITLED</text>
      </svg>
    </header>

    <p class="intro">
      Lorem ipsum dolor sit amet, consectetur adipiscing elit. Curabitur si<br>
      t amet lacus quis lectus suscipit mollis. Morbi varius ullamcorper fermentum. Nulla in nisi<br>
      eu enim vulputate hendrerit. Nullam faucibus egestas molestie. Ut a libero at odio
    </p>

    <p class="dates">7-27 June 2013, Location St.</p>
    <p class="dates-note">aucibus egestas molestie. Ut a libero at odio</p>

    <div class="web-bar"></div>
    <p class="web-address">www.yourwebsite.com</p>
  </main>
</body>
</html>
```